Travel Blogger Business Card for wanderquill.net

I need a two-sided business card for a travel blogging website. The card should be both professional and fun at the same time. This is for the website www.wanderquill.net

I don't necessarily think that the current logo on the website needs to be used on the business card but it can be. I am very flexible with ideas

Target Market(s)

Travel agencies that will be met at a conference.

Industry/Entity Type

Travel

Contact Information for Business Card

Company Name: Wander Quill.net
Name: Marcel Vennor
Voice: +1-(345)-555-0193
Address: Coral Reed Shore, Grand Cayman, Cayman Islands
Email: ceo@wanderquill.net

Colors
0592cd
0355a3
3176b5
33a6d7
85cae6
85acd3

Requirements
Must have
• Website address and name should be bigger than address, phone number, and email.

```html
<!DOCTYPE html>
<html lang="en">
<head>
<meta charset="utf-8">
<title>Wander Quill.net – Business Card Back</title>
<link rel="stylesheet" href="https://fonts.googleapis.com/css2?family=Montserrat:wght@200;800&display=swap">
<style>
  :root {
    --card-blue: #0a44f8;
    --ink-white: #ffffff;
  }
  * { margin: 0; padding: 0; box-sizing: border-box; }
  html, body {
    width: 1200px;
    height: 734px;
    overflow: hidden;
    background: var(--card-blue);
  }
  .card {
    position: relative;
    width: 1200px;
    height: 734px;
    background: var(--card-blue);
    font-family: "Montserrat", sans-serif;
    color: var(--ink-white);
  }
  .web-frame {
    position: absolute;
    left: 140px;
    top: 309px;
    width: 920px;
    height: 119px;
    border: 2px solid var(--ink-white);
    border-radius: 10px;
    display: flex;
    align-items: center;
    justify-content: center;
  }
  .web-address {
    font-weight: 200;
    font-size: 80px;
    line-height: 1;
    letter-spacing: 0.5px;
    margin-top: -4px;
    white-space: nowrap;
  }
  .brand {
    position: absolute;
    left: 0;
    right: 0;
    top: 646px;
    display: flex;
    align-items: center;
    justify-content: center;
    gap: 12px;
  }
  .brand-dot {
    width: 36px;
    height: 36px;
    border-radius: 50%;
    background: var(--ink-white);
  }
  .brand-name {
    font-weight: 800;
    font-size: 32px;
    line-height: 1;
    letter-spacing: 0;
    text-transform: uppercase;
    white-space: nowrap;
  }
</style>
</head>
<body>
  <main class="card">
    <div class="web-frame">
      <p class="web-address">www.wanderquill.net</p>
    </div>
    <div class="brand">
      <span class="brand-dot"></span>
      <span class="brand-name">Wander Quill</span>
    </div>
  </main>
</body>
</html>
```